French Puns

Creation of a cover for a book on French plays on words.
The public is lovers of the French language
TITLE: The gentle phrases of Honoré Vasseline
SUB-TITLE: Clever turns, turns of phrase
PUBLISHER (at the bottom of the page): Editions Plumeau
(See joined examples, previous books of the same author)
Size: 14 x 20.5 cm
Please note that the text on the cover is in French, not in English:
Fine phrases from Honoré Vasseline
Witty words, witty words (subtitle, smaller)
Plumeau Editions

```html
<!DOCTYPE html>
<html lang="fr">
<head>
<meta charset="utf-8">
<title>Les doux propos — Honoré Vasseline</title>
<link rel="stylesheet" href="https://fonts.googleapis.com/css2?family=Alegreya:wght@500&family=Marcellus&family=Montserrat:wght@400&display=swap">
<style>
  :root {
    --backdrop: #545454;
    --paper: #fbfbfb;
    --title-red: #a10a0b;
    --ink-brown: #2e1f17;
    --sketch-light: #e6e1dc;
    --sketch-dark: #b9ada3;
  }
  * { margin: 0; padding: 0; box-sizing: border-box; }
  html, body {
    width: 1200px;
    height: 1042px;
    overflow: hidden;
    background: var(--backdrop);
  }
  .book-cover {
    position: absolute;
    left: 280px;
    top: 52px;
    width: 640px;
    height: 938px;
    background: var(--paper);
    text-align: center;
    color: var(--ink-brown);
  }
  .author {
    position: absolute;
    top: 76px;
    left: 0;
    width: 100%;
    font-family: "Marcellus", serif;
    font-size: 44px;
    letter-spacing: 0.5px;
  }
  .title {
    position: absolute;
    top: 138px;
    left: 0;
    width: 100%;
    font-family: "Alegreya", serif;
    font-weight: 500;
    font-size: 124px;
    line-height: 100px;
    letter-spacing: -3px;
    color: var(--title-red);
  }
  .title span { display: block; }
  .subtitle {
    position: absolute;
    top: 405px;
    left: 0;
    width: 100%;
    font-family: "Montserrat", sans-serif;
    font-size: 33px;
    letter-spacing: 0.2px;
  }
  .illustration {
    position: absolute;
    top: 484px;
    left: 245px;
    width: 150px;
    height: 322px;
  }
  .publisher {
    position: absolute;
    top: 884px;
    left: 0;
    width: 100%;
    font-family: "Montserrat", sans-serif;
    font-size: 24px;
    letter-spacing: 1.2px;
  }
</style>
</head>
<body>
  <main class="book-cover">
    <p class="author">Honoré Vasseline</p>
    <h1 class="title"><span>Les doux</span><span>propos</span></h1>
    <p class="subtitle">Clever turns, turns of phrase</p>
    <svg class="illustration" viewBox="0 0 150 322" role="img" aria-label="Pen sketch of a juggler in a top hat and striped shirt riding a unicycle while tossing three balls">
      <defs>
        <linearGradient id="sketch-tone" x1="0" y1="0" x2="0" y2="1">
          <stop offset="0" stop-color="#e6e1dc"/>
          <stop offset="1" stop-color="#b9ada3"/>
        </linearGradient>
      </defs>
      <rect x="0" y="0" width="150" height="322" rx="16" fill="url(#sketch-tone)"/>
    </svg>
    <p class="publisher">Editions Plumeau</p>
  </main>
</body>
</html>
```